TrueNest Realty needs a business card design.

Please view my website at www.truenestrealty.example to learn about my business and my marketing style. I need a business template...one where I can change the names for all my employees. I'm hoping two find 2 designs that I like so my agents have a choice.

We're a real estate company. Instead of the standard self portraits that other Realtors use, we use monkeys. I need it two sided.... need to have our logo, monkey pic, agents name & info. Don't need room for a physical address, just name, title, phone number, email, website address.

Need the tagline: Don't Let Them Make a Monkey Out of You!

Corinne Whitlake ABR, GRI
Exclusive Buyer Broker
TrueNest Realty

214-555-0172
Corinne@TrueNestRealty.example
www.TrueNestRealty.example

Attached our logo and a couple of monkey pics. It's okay to crop the monkey, but the monkey needs to be a dominate part of the card. I actually almost prefer a head shot of the monkey but I'm open. I've also attached some designs that I like.
Updates

MUST have the tagline: Don't Let Them Make a Monkey Out of You!

Project Deadline Extended
Reason: Change to committed funds.

Industry/Entity Type

Real Estate

Requirements
Must have
• Must have my tagline below on the card:

Don't Let Them Make a Monkey Out of You!

Use 2 different monkey pics attached.
Nice to have
• I'd like to change the bow lipstick color on the monkey to red.

```html
<!DOCTYPE html>
<html lang="en">
<head>
<meta charset="utf-8">
<title>TrueNest Realty – Business Card</title>
<link rel="stylesheet" href="https://fonts.googleapis.com/css2?family=Arimo:wght@400;700&display=swap">
<style>
  :root {
    --page-bg: #e9e9ec;
    --card-white: #ffffff;
    --navy: #1a1f8c;
    --navy-deep: #0c1170;
    --brand-red: #e3262f;
    --ink-navy: #2a2f7a;
    --fur-dark: #3a2a22;
    --fur-mid: #6b4e3d;
  }
  * { box-sizing: border-box; margin: 0; padding: 0; }
  html, body {
    width: 1200px; height: 900px; overflow: hidden;
    background: var(--page-bg);
    font-family: "Arimo", Arial, sans-serif;
  }
  .canvas {
    width: 1200px; height: 900px;
    display: flex; justify-content: center; align-items: center; gap: 80px;
  }
  .card {
    position: relative;
    width: 400px; height: 700px;
    background: var(--card-white);
    border-radius: 18px;
    overflow: hidden;
    box-shadow: 0 10px 30px rgba(0,0,0,.18);
  }

  /* Back: tagline + agent details */
  .card-back .tagline-area {
    position: absolute; top: 40px; left: 0; right: 0;
    display: flex; flex-direction: column; align-items: center;
  }
  .card-back .monkey-small {
    width: 170px; height: 110px; border-radius: 50%;
    background: radial-gradient(ellipse at 50% 45%, var(--fur-mid) 0%, var(--fur-dark) 75%);
  }
  .card-back .tagline {
    margin-top: 24px;
    font-size: 19px; line-height: 1.35;
    color: var(--ink-navy); text-align: center;
  }
  .card-back .curve {
    position: absolute; left: 0; bottom: 0; width: 400px; height: 460px;
  }
  .card-back .details {
    position: absolute; left: 40px; right: 30px; bottom: 60px;
    color: #fff;
  }
  .details .agent-name { font-size: 30px; font-weight: 700; }
  .details .agent-title { font-size: 21px; margin-top: 6px; }
  .details .contact { list-style: none; margin-top: 36px; font-size: 17px; line-height: 1.55; }

  /* Front: sideways brand + hero monkey */
  .card-front .brand {
    position: absolute; left: 34px; bottom: 60px;
    display: flex; align-items: center; gap: 12px;
    writing-mode: vertical-rl; transform: rotate(180deg);
  }
  .brand .brand-mark { width: 14px; height: 14px; background: var(--brand-red); }
  .brand .brand-name { font-size: 32px; font-weight: 700; color: var(--navy); white-space: nowrap; }
  .card-front .monkey-hero {
    position: absolute; top: 70px; left: 120px; width: 240px; height: 560px;
    border-radius: 120px 120px 60px 60px;
    background: linear-gradient(180deg, var(--fur-mid) 0%, var(--fur-dark) 55%, #2a1d17 100%);
  }
</style>
</head>
<body>
<main class="canvas">

  <section class="card card-back">
    <div class="tagline-area">
      <div class="monkey-small" role="img" aria-label="Small illustration of a chimpanzee holding two paintbrushes"></div>
      <p class="tagline">Don't Let Them Make a Monkey<br>Out of You!</p>
    </div>
    <svg class="curve" viewBox="0 0 400 460" aria-hidden="true">
      <path d="M0 70 Q220 10 400 110 L400 460 L0 460 Z" fill="var(--brand-red)"/>
      <path d="M0 84 Q220 26 400 124 L400 460 L0 460 Z" fill="var(--navy)"/>
      <path d="M0 300 Q200 260 400 330 L400 460 L0 460 Z" fill="var(--navy-deep)" opacity=".35"/>
    </svg>
    <div class="details">
      <h1 class="agent-name">Corinne Whitlake</h1>
      <p class="agent-title">Exclusive Buyer Broker</p>
      <ul class="contact">
        <li>214-555-0172</li>
        <li>Corinne@TrueNestRealty.example</li>
        <li>www.TrueNestRealty.example</li>
      </ul>
    </div>
  </section>

  <section class="card card-front">
    <div class="brand">
      <span class="brand-mark"></span>
      <span class="brand-name">TrueNest Realty</span>
    </div>
    <div class="monkey-hero" role="img" aria-label="Large illustration of a grinning chimpanzee with a pink bow, standing with hands on hips"></div>
  </section>

</main>
</body>
</html>
```